Plakat-Design für Vogelvolieren
Zielgruppe
Es geht um vier Din A4-Plakate, die an vier Vogelvolieren hängen und Informationen zu den Vögeln bieten, die sich in den Volieren befinden.
Die Volieren gehören zum Wildpark Kernbachtal. Einem kleinen Wildpark, bei dem ausschließlich Ehrenamtliche tätig sind. Der Eintritt ist frei.
Die Zielgruppe sind die Besucher - von klein bis groß, von jung bis alt
Aufgabenstellung
Gute Lesbarkeit, denn die Informationsvermittlung soll im Vordergrund stehen.
Wir benötigen 1 Plakatdesign und die offenen Daten in InDesign, denn dann würden wir bei den weiteren drei Plakaten die Texte und Fotos austauschen.
Es sind 2 Plakate mit 4 Vögeln und 2 Plakate mit 2 Vögeln.

```html
<!DOCTYPE html>
<html lang="de">
<head>
<meta charset="utf-8">
<title>Zebrafink – Wildpark Kernbachtal</title>
<link rel="stylesheet" href="https://fonts.googleapis.com/css2?family=Caveat+Brush&family=Fira+Sans+Condensed:wght@500;600&family=Quicksand:wght@400&display=swap">
<style>
  :root {
    --purple: #a0306e;
    --green: #4fa165;
    --orange: #e0913f;
    --paper: #e7e7e7;
    --white: #f4f4f4;
    --ink: #262626;
    --photo-light: #e2bf88;
    --photo-dark: #c4965a;
  }
  html, body {
    margin: 0;
    width: 1200px;
    height: 1200px;
    overflow: hidden;
    background: #d6d6d6;
  }
  .stage {
    position: relative;
    width: 1200px;
    height: 1200px;
  }
  .poster {
    position: absolute;
    left: 196px;
    top: 30px;
    width: 1140px;
    height: 1610px;
    transform: scale(0.7081);
    transform-origin: 0 0;
    background: var(--paper);
    overflow: hidden;
    font-family: "Fira Sans Condensed", "Arial Narrow", sans-serif;
    color: var(--ink);
    box-shadow: 0 6px 24px rgba(0,0,0,0.18);
  }
  .poster-shapes {
    position: absolute;
    inset: 0;
    width: 1140px;
    height: 1610px;
  }
  .species-latin {
    font-family: "Quicksand", sans-serif;
    font-size: 31px;
    fill: var(--white);
  }
  .park-name {
    position: absolute;
    right: 30px;
    top: 70px;
    display: flex;
    align-items: center;
    gap: 14px;
    font-weight: 600;
    font-size: 36px;
    color: var(--purple);
  }
  .park-name .dot {
    width: 22px;
    height: 22px;
    border-radius: 50%;
    background: var(--green);
  }
  .species-title {
    position: absolute;
    left: 72px;
    top: 505px;
    margin: 0;
    font-family: "Caveat Brush", cursive;
    font-weight: 400;
    font-size: 134px;
    line-height: 1;
    color: var(--white);
    transform: rotate(-3deg);
    white-space: nowrap;
  }
  .section-heading {
    margin: 0 0 14px;
    font-weight: 600;
    font-size: 38px;
    color: var(--purple);
    text-decoration: underline;
    text-decoration-thickness: 2px;
    text-underline-offset: 6px;
  }
  .section-text {
    margin: 0;
    font-weight: 500;
    font-size: 30px;
    line-height: 39px;
  }
  .appearance {
    position: absolute;
    left: 45px;
    top: 895px;
    width: 570px;
    text-align: center;
  }
  .map-placeholder {
    position: absolute;
    left: 720px;
    top: 920px;
    width: 300px;
    height: 150px;
    border-radius: 10px;
    background: linear-gradient(135deg, var(--green) 0%, #62ad75 75%, var(--purple) 100%);
  }
  .occurrence {
    position: absolute;
    left: 700px;
    top: 1108px;
    width: 355px;
    text-align: center;
  }
  .call-note {
    position: absolute;
    left: 612px;
    top: 1468px;
    width: 510px;
    margin: 0;
    text-align: center;
    font-weight: 500;
    font-size: 29px;
    line-height: 39px;
    color: var(--white);
  }
  .accent-dot {
    position: absolute;
    left: 70px;
    top: 1505px;
    width: 60px;
    height: 60px;
    border-radius: 50%;
    background: var(--orange);
  }
</style>
</head>
<body>
<div class="stage">
  <article class="poster">
    <svg class="poster-shapes" viewBox="0 0 1140 1610">
      <defs>
        <linearGradient id="photoTone" x1="0" y1="0" x2="1" y2="1">
          <stop offset="0" stop-color="var(--photo-light)"/>
          <stop offset="0.6" stop-color="#d7ae72"/>
          <stop offset="1" stop-color="var(--photo-dark)"/>
        </linearGradient>
      </defs>

      <path d="M640,0 H1140 V190 C1050,180 960,185 870,172 C760,160 690,110 640,0 Z" fill="var(--white)"/>

      <path role="img" aria-label="Foto: Zebrafink-Männchen auf einer Sitzstange in der Voliere"
            d="M0,0 H640 C690,110 760,160 870,172 C960,185 1050,180 1140,190 V640 C980,760 780,785 560,735 C350,690 150,700 0,790 Z"
            fill="url(#photoTone)"/>

      <path d="M640,0 H690 C720,90 780,145 870,165 C960,180 1050,176 1140,182 V190 C1050,180 960,185 870,172 C760,160 690,110 640,0 Z" fill="var(--orange)"/>

      <path d="M40,600 C60,480 150,440 250,455 C350,470 430,540 590,535 C560,620 480,700 350,700 C220,705 80,690 25,725 C20,690 25,640 40,600 Z" fill="var(--purple)"/>

      <path d="M0,790 C150,700 350,690 560,735 C780,785 980,760 1140,640 V830 C980,880 820,840 650,805 C350,790 120,820 0,920 Z" fill="var(--orange)"/>
      <path d="M0,790 C150,700 350,690 560,735 C780,785 980,760 1140,640 V830 C980,880 820,840 650,805 C400,760 150,760 0,815 Z" fill="var(--green)"/>

      <path id="latinPath" d="M675,806 C800,850 960,850 1132,774" fill="none"/>
      <text class="species-latin"><textPath href="#latinPath" textLength="450" lengthAdjust="spacingAndGlyphs">Taeniopygia guttata castanotis</textPath></text>

      <path d="M820,1372 C940,1350 1040,1340 1140,1340 V1378 C1040,1385 940,1395 820,1372 Z" fill="var(--orange)"/>
      <path d="M440,1610 C500,1500 600,1420 820,1398 C950,1385 1050,1380 1140,1378 V1610 Z" fill="var(--green)"/>
    </svg>

    <div class="park-name"><span class="dot"></span>Wildpark Kernbachtal</div>

    <h1 class="species-title">Zebrafink</h1>

    <section class="appearance">
      <h2 class="section-heading">Aussehen:</h2>
      <p class="section-text">Gut zu erkennen sind Zebrafinken an<br>ihrem orange-roten Schnabel, am<br>schwarzen Tränenstrich unter den Augen<br>und der schwarzen Zebra-Musterung der<br>Brust.<br>Das Gefieder der Männchen, die über<br>einen orange-farbenen Wangenfleck<br>verfügen, ist kräftiger als das der<br>Weibchen. Ihre kurzen, eckigen Flügel<br>machen Zebrafinken zu wahren<br>Flugakrobaten.<br>Zebrafinken werden rund 12 Zentimeter<br>lang und wiegen 12 bis 14 Gramm.</p>
    </section>

    <div class="map-placeholder" role="img" aria-label="Weltkarte mit hervorgehobenem Australien"></div>

    <section class="occurrence">
      <h2 class="section-heading">Vorkommen:</h2>
      <p class="section-text">Australische Zebrafinken<br>leben fast überall in<br>Australien.</p>
    </section>

    <p class="call-note">Typisch ist der quakende Kontaktruf<br>beider Geschlechter und der schlichte,<br>zwitschernde Gesang der Hähne.</p>

    <span class="accent-dot"></span>
  </article>
</div>
</body>
</html>
```